Production Co Needs Movie Poster for Supernatural Thriller

Hi, we need a poster designed for a film we're going to be pitching and raising finance for. The film is a supernatural thriller called "Lanterns Beneath the Stair", a story told from the perspective of the ghosts - a father and his 8 year old son. References include 'When Frost Forgets' (reference poster attached) and 'The Widow's Lantern' - not blood and gore but creepy and atmospheric. We're looking for a design that will capture the imagination and make people want to know more and see the movie!

Synopsis:
When the sudden deaths of young Tobias and his father render them as ghosts, they’re thrust into a dangerous new reality of amateur clairvoyants, determined ghost hunters, and lost souls; a plane of existence where they must survive both the living and the dead.

Industry/Entity Type

Finance

Requirements
Nice to have
• It would be nice to include the father/son imagery perhaps in silhouette. Open to ideas. The film is a psychological thriller as much as a ghost story so it would be good to include that element rather than a 'traditional horror' style poster.
• Alternatively a simple, striking image with the title would also be great - see Velmar poster attached as a reference,
• ALSO - the entire film takes place inside the house.
Should not have
• No screaming faces please.

```html
<!DOCTYPE html>
<html lang="en">
<head>
<meta charset="utf-8">
<title>Lanterns Beneath the Stair — Poster</title>
<link rel="stylesheet" href="https://fonts.googleapis.com/css2?family=Cinzel:wght@500&display=swap">
<style>
  :root {
    --sepia-deep: #1c150c;
    --sepia-mid: #5a4a33;
    --sepia-light: #a08a66;
    --sepia-glow: #c9b48f;
    --title-parchment: #ead6a6;
    --frame-edge: #0e0a05;
  }
  html, body {
    margin: 0;
    padding: 0;
    width: 810px;
    height: 1200px;
    overflow: hidden;
    background: var(--frame-edge);
  }
  .poster {
    position: relative;
    width: 810px;
    height: 1200px;
    overflow: hidden;
  }
  .staircase-scene {
    position: absolute;
    inset: 0;
    background:
      radial-gradient(ellipse 38% 30% at 50% 30%, var(--sepia-glow) 0%, rgba(160,138,102,0.55) 45%, rgba(90,74,51,0) 100%),
      linear-gradient(180deg, var(--sepia-mid) 0%, var(--sepia-light) 28%, var(--sepia-mid) 55%, var(--sepia-deep) 100%);
  }
  .edge-burn {
    position: absolute;
    inset: 0;
    background: radial-gradient(ellipse 70% 62% at 50% 50%, rgba(0,0,0,0) 55%, rgba(14,10,5,0.75) 88%, var(--frame-edge) 100%);
    box-shadow: inset 0 0 0 14px rgba(14,10,5,0.85);
  }
  .title {
    position: absolute;
    inset: 0;
    width: 810px;
    height: 1200px;
  }
  .title text {
    font-family: "Cinzel", "Trajan Pro", Georgia, serif;
    font-weight: 500;
    fill: var(--title-parchment);
    text-anchor: middle;
  }
</style>
</head>
<body>
  <main class="poster">
    <div class="staircase-scene" role="img" aria-label="Sepia photograph of a grand wooden staircase with carved banisters, a faint ghostly figure standing at the top landing"></div>
    <div class="edge-burn"></div>
    <svg class="title" viewBox="0 0 810 1200" aria-label="Lanterns Beneath the Stair">
      <text class="title-line title-line--first" x="405" y="210" font-size="186" textLength="700" lengthAdjust="spacingAndGlyphs">LANTERNS</text>
      <text class="title-line title-line--second" x="405" y="415" font-size="243" textLength="700" lengthAdjust="spacingAndGlyphs">BENEATH</text>
      <text class="title-line title-line--third" x="405" y="700" font-size="357" textLength="700" lengthAdjust="spacingAndGlyphs">THE</text>
      <text class="title-line title-line--fourth" x="405" y="1110" font-size="528" textLength="700" lengthAdjust="spacingAndGlyphs">STAIR</text>
    </svg>
  </main>
</body>
</html>
```